Website redesign for a national printing company

Our current website is dated and boring: ferngladeflags.com

We are looking for a fresh, modern design. We need a clean, minimal design that is also elegant, really shows off large, bright photos of our banners in action and POPS. Our goal is to showcase our beautiful banners, while also giving the user the confidence in our company that we will provide friendly, fast service, fast printing, and deliver their banners on time for their event.

I want a nice flow to the website, the design should tie in well with the printing feel. Here is an example of clean, beautiful design that ties in to the industry - https://www.vorpa.com/ - notice how the buttons are like chat icons, for example.

More examples:

Nice clean design https://www.quilbex.com/

https://tavrimo.com/ nice and clean, but it POPS really well.

I like https://www.prendavel.com/

https://www.ubrato.com/ gorgeous site, clean, modern

Beautiful, simple, clean, modern - https://mirevolta.com/en-us/

These websites are not from the print industry, that’s because most printers don’t have good websites - they are more focused on local businesses, referrals, not really online marketing.

But keep in mind in your design that we need to give the feel that we are printing their banners beautifully, fast, with great service.

https://www.faywendle.com/ so clean, bold, clear to the user what the company does. Love this simple yet elegant design.

https://www.k7.com/ - so pretty! And still so simple and obvious to the user what to do on their site.

https://zulvane.com/

https://quenbrisk.com/us/en/ big and bold - yet super nicely designed with so many nice touches

https://posterlyn.com/ - also clean, simple, and so obvious to the user to take action and contact the company
Updates

I just updated the job brief, and you can also view it in full here - https://files.oskavimo.com/document/d/7Hrp2LmQz94VtNcXe0BgYsJd1KwFu63aPoE8iRnCTyUZ/edit?usp=sharing

Target Market(s)

Please read this customer persona - https://files.oskavimo.com/document/d/7Hrp2LmQz94VtNcXe0BgYsJd1KwFu63aPoE8iRnCTyUZ/edit?usp=sharing

Industry/Entity Type

Printing

Number of Pages Required

1 page

Requirements
Must have
• Nice flow to the website, the design should tie in well with the printing feel. Here is an example of clean, beautiful design that ties in to the industry - https://www.vorpa.com/ - notice how the buttons are like chat icons, for example.
Should not have
• No filters on the images, we want large, beautiful images.

```html
<!DOCTYPE html>
<html lang="en">
<head>
<meta charset="utf-8">
<title>Fernglade Flags</title>
<link href="https://fonts.googleapis.com/css2?family=Outfit:wght@400;500;600;700&family=Arimo:wght@400;700&display=swap" rel="stylesheet">
<style>
:root{
  --blue:#1f4fd1;
  --ink:#111318;
  --body:#4a4d55;
  --panel:#eef2fb;
  --band:#edf1fb;
  --footer:#1c1d21;
  --white:#ffffff;
  --star:#f6b20b;
}
*{box-sizing:border-box;margin:0;padding:0}
html,body{width:1200px;height:3188px;overflow:hidden}
body{position:relative;background:var(--white);font-family:"Arimo",Arial,sans-serif;color:var(--ink)}
.abs{position:absolute}
.blue{color:var(--blue)}

/* hero */
.hero{left:0;top:0;width:1200px;height:712px;clip-path:polygon(0 0,100% 0,100% 100%,0 89.8%);
  background:
    radial-gradient(ellipse 420px 220px at 560px 330px,#6b6d78 0%,rgba(107,109,120,0) 70%),
    radial-gradient(ellipse 260px 200px at 1010px 300px,#d9e4ef 0%,rgba(217,228,239,0) 70%),
    linear-gradient(180deg,#26402b 0%,#3a5a3a 22%,#4a4c5c 50%,#8a7468 75%,#b39d8d 100%)}
.hero::after{content:"";position:absolute;inset:0;background:linear-gradient(90deg,rgba(8,12,18,.55),rgba(8,12,18,0) 60%)}
.nav{top:18px;left:60px;width:1080px;height:50px;display:flex;align-items:center;z-index:2}
.logo{font-family:"Outfit",sans-serif;font-weight:600;color:var(--white);font-size:31px;line-height:1}
.logo small{display:block;font-size:13px;letter-spacing:9px;font-weight:400;text-align:center;margin-top:2px}
.menu{display:flex;gap:26px;margin-left:44px;color:var(--white);font-size:13px}
.phone{margin-left:auto;color:var(--white);font-size:13px;display:flex;align-items:center;gap:7px}
.phone b{font-weight:700}
.btn{display:inline-flex;align-items:center;gap:10px;font-size:13px;border-radius:7px;height:36px;padding:0 16px;color:var(--white)}
.btn-ghost{border:1px solid rgba(255,255,255,.85);margin-left:20px}
.btn-solid{background:var(--blue);margin-left:10px}
.hero-copy{left:61px;top:222px;z-index:2;color:var(--white)}
.hero-copy h1{font-family:"Outfit",sans-serif;font-weight:600;font-size:46px;line-height:52px;width:520px}
.hero-copy p{font-size:13px;line-height:21px;width:400px;margin-top:22px}
.hero-copy .btn{margin-top:22px;height:40px;padding:0 20px}

.sec-title{width:1200px;left:0;text-align:center;font-family:"Outfit",sans-serif;font-weight:600;font-size:34px}

/* brands */
.brands{left:150px;top:855px;width:900px;display:flex;justify-content:space-between;align-items:center}
.brand{display:flex;align-items:center;gap:6px;font-family:"Outfit",sans-serif;font-weight:700;font-size:16px;color:var(--ink)}
.brand i{display:block;width:20px;height:20px;border-radius:50%;background:var(--ink)}

/* products */
.products{left:60px;top:982px;width:1080px;height:600px;background:var(--panel);border-radius:28px}
.cards{left:68px;top:1124px;display:flex;gap:17px}
.card{width:254px;height:391px;background:var(--white);border-bottom:2px solid var(--blue);position:relative}
.card .ph{height:180px}
.card h3{font-family:"Outfit",sans-serif;font-weight:500;font-size:18px;line-height:24px;padding:22px 12px 0;height:80px;width:220px}
.card p{font-size:11px;line-height:21px;color:var(--body);padding:0 13px;height:84px}
.card a{position:absolute;left:13px;top:358px;font-size:11.5px;font-weight:700;color:var(--blue);display:flex;gap:8px;align-items:center;text-decoration:none}

/* process */
.steps{left:60px;top:1772px;width:1080px}
.step{position:absolute;width:180px;text-align:center;font-family:"Outfit",sans-serif;font-weight:500;font-size:16px;line-height:24px}
.step svg{display:block;margin:0 auto 18px}
.dots{position:absolute;top:40px;width:125px;height:10px}

/* reviews */
.band{left:0;top:1955px;width:1200px;height:884px;background:var(--band);clip-path:polygon(0 0,100% 8.4%,100% 100%,0 100%)}
.sub{left:0;width:1200px;top:2122px;text-align:center;font-size:12.5px;line-height:21px;color:var(--body)}
.review{width:340px;height:270px;background:var(--white);border-radius:10px;padding:34px 28px 0}
.stars{display:flex;gap:4px}
.ago{font-family:"Outfit",sans-serif;font-size:12px;color:#777;margin-top:6px}
.review p{font-size:12.5px;line-height:21px;color:var(--body);margin-top:8px;height:92px;width:265px}
.review p span{color:var(--blue)}
.who{display:flex;align-items:center;gap:16px;margin-top:14px;font-family:"Outfit",sans-serif;font-weight:600;font-size:16px}
.av{width:58px;height:58px;border-radius:50%;flex:none}
.av-t{background:#6f8591;color:var(--white);display:flex;align-items:center;justify-content:center;font-size:24px;font-weight:500}

/* footer */
.footer{left:0;top:2837px;width:1200px;height:351px;background:var(--footer);color:var(--white)}
.f-logo{left:60px;top:56px;font-family:"Outfit",sans-serif;font-weight:600;font-size:38px;color:var(--blue);line-height:1}
.f-logo small{display:block;font-size:14px;letter-spacing:12px;text-align:center;font-weight:400}
.f-about{left:61px;top:128px;width:250px;font-size:12px;line-height:21px}
.col{top:66px;font-size:12.5px}
.col h4{font-family:"Outfit",sans-serif;font-weight:500;font-size:15px;color:var(--blue);margin-bottom:12px}
.col li{list-style:none;line-height:26px}
.col .ci{display:flex;align-items:center;gap:14px;line-height:31px}
.copy{left:61px;top:314px;font-size:11.5px}
.social{left:1022px;top:303px;display:flex;gap:10px}
.social span{width:32px;height:32px;border-radius:50%;background:var(--white);color:var(--ink);font-family:"Outfit",sans-serif;font-weight:600;font-size:13px;display:flex;align-items:center;justify-content:center}
.social span:first-child{background:var(--blue);color:var(--white)}
</style>
</head>
<body>

<div class="abs hero" role="img" aria-label="Photo of an outdoor music festival stage with large sponsor banners overhead and a big seated crowd under white tents"></div>

<header class="abs nav">
  <div class="logo">Fernglade<small>FLAGS</small></div>
  <nav class="menu"><span>About</span><span>Products ⌄</span><span>Galleries ⌄</span><span>Contact Us</span></nav>
  <div class="phone">
    <svg width="16" height="16" viewBox="0 0 24 24" fill="none" stroke="#fff" stroke-width="1.6"><path d="M5 3h4l2 5-2.5 1.5a11 11 0 0 0 6 6L16 13l5 2v4a2 2 0 0 1-2 2A16 16 0 0 1 3 5a2 2 0 0 1 2-2z"/></svg>
    Toll free: <b>800-555-0142</b>
  </div>
  <span class="btn btn-ghost">Get A Quote <svg width="18" height="10" viewBox="0 0 18 10" fill="none" stroke="#fff" stroke-width="1.5"><path d="M0 5h16M12 1l4 4-4 4"/></svg></span>
  <span class="btn btn-solid">Upload <svg width="18" height="10" viewBox="0 0 18 10" fill="none" stroke="#fff" stroke-width="1.5"><path d="M0 5h16M12 1l4 4-4 4"/></svg></span>
</header>

<div class="abs hero-copy">
  <h1>We Provide Faster Service, printing and Deliver their banners</h1>
  <p>Lorem Ipsum is simply dummy text of the printing and typesetting industry.Lorem Ipsum has been the industry's</p>
  <span class="btn btn-solid" style="margin-left:0">Get A Quote <svg width="18" height="10" viewBox="0 0 18 10" fill="none" stroke="#fff" stroke-width="1.5"><path d="M0 5h16M12 1l4 4-4 4"/></svg></span>
</div>

<h2 class="abs sec-title" style="top:754px">Loved by <span class="blue">brands</span></h2>
<div class="abs brands">
  <div class="brand"><i></i>Brightcast</div>
  <div class="brand"><i></i>Lumenwave Media</div>
  <div class="brand">Harbor City Comets</div>
  <div class="brand">Echoline Media</div>
  <div class="brand">Jesse Marlow</div>
  <div class="brand">Velmora</div>
</div>

<div class="abs products"></div>
<h2 class="abs sec-title" style="top:1048px">Our <span class="blue">Products</span></h2>
<div class="abs cards">
  <article class="card">
    <div class="ph" role="img" aria-label="Photo of black plastic roll banners wrapped on barricades at a street fair with red tents" style="background:linear-gradient(180deg,#dfe6ea 0%,#b8c0c4 30%,#b8433f 45%,#2a2628 62%,#3b3537 85%,#9a9c9e 100%)"></div>
    <h3>Plastic Roll Banners</h3>
    <p>Plastic roll banners are the perfect solution for planners and advertisers looking to cover their event with a logo or branding message on budget...</p>
    <a>Read More <svg width="18" height="10" viewBox="0 0 18 10" fill="none" stroke="#1f4fd1" stroke-width="1.5"><path d="M0 5h16M12 1l4 4-4 4"/></svg></a>
  </article>
  <article class="card">
    <div class="ph" role="img" aria-label="Photo of a festival stage with a printed mesh banner header and stage backdrop above a crowd" style="background:linear-gradient(180deg,#7fb3e6 0%,#5d8fcf 25%,#c9a85a 45%,#5a4a3c 70%,#2e2622 100%)"></div>
    <h3>Festival Mesh Banners and Stage Backdrops</h3>
    <p>The perfect solution for outdoor (or indoor) events - on budget. Our broad range of materials, colors, sizes and large format printing capabilities</p>
    <a>Read More <svg width="18" height="10" viewBox="0 0 18 10" fill="none" stroke="#1f4fd1" stroke-width="1.5"><path d="M0 5h16M12 1l4 4-4 4"/></svg></a>
  </article>
  <article class="card">
    <div class="ph" role="img" aria-label="Photo of a large green format mesh banner for a charity run hung on a building facade" style="background:linear-gradient(180deg,#8fa3b3 0%,#9fb03c 25%,#c3cf4a 50%,#5c7fa8 70%,#3f6590 100%)"></div>
    <h3>Large Format and Mesh Banners</h3>
    <p>The perfect marketing solution for large format coverage - on budget. Customiz- able at any size, our blend of materials provide all the necessary.</p>
    <a>Read More <svg width="18" height="10" viewBox="0 0 18 10" fill="none" stroke="#1f4fd1" stroke-width="1.5"><path d="M0 5h16M12 1l4 4-4 4"/></svg></a>
  </article>
  <article class="card">
    <div class="ph" role="img" aria-label="Photo of a colourful cloth backdrop behind a band's stage with drums" style="background:linear-gradient(180deg,#3a4fa3 0%,#6a4f9a 35%,#c46d7d 55%,#3d3f80 75%,#1a1b2a 100%)"></div>
    <h3>Cloth Banners and Cloth Backdrops</h3>
    <p>Cloth banners are the ultimate gold standard in backdrop printing. With vibrant color representation, high definition colors and the lightest</p>
    <a>Read More <svg width="18" height="10" viewBox="0 0 18 10" fill="none" stroke="#1f4fd1" stroke-width="1.5"><path d="M0 5h16M12 1l4 4-4 4"/></svg></a>
  </article>
</div>

<h2 class="abs sec-title" style="top:1690px">Our Process Is <span class="blue">Fast and Simple</span></h2>
<div class="abs steps">
  <div class="step" style="left:18px;top:0">
    <svg width="56" height="72" viewBox="0 0 56 72" fill="none" stroke="#1a1a1a" stroke-width="2.4"><path d="M4 4h34l14 14v50H4z"/><path d="M38 4v14h14"/><path d="M28 56V32M18 42l10-10 10 10" stroke="#1f4fd1"/></svg>
    Upload Art Files
  </div>
  <svg class="dots" style="left:188px" viewBox="0 0 125 10" fill="none" stroke="#6d8ae0" stroke-width="1.2"><path d="M0 5h122" stroke-dasharray="2 3"/><path d="M119 1l4 4-4 4"/></svg>
  <div class="step" style="left:297px;top:0">
    <svg width="72" height="72" viewBox="0 0 72 72" fill="none" stroke="#1a1a1a" stroke-width="2.4"><path d="M4 30l10-8h44l10 8v36H4z"/><path d="M4 30l32 20 32-20"/><path d="M36 4v28M26 22l10 10 10-10" stroke="#1f4fd1"/></svg>
    Receive A proof In Your Inbox
  </div>
  <svg class="dots" style="left:460px" viewBox="0 0 125 10" fill="none" stroke="#6d8ae0" stroke-width="1.2"><path d="M0 5h122" stroke-dasharray="2 3"/><path d="M119 1l4 4-4 4"/></svg>
  <div class="step" style="left:576px;top:0">
    <svg width="76" height="72" viewBox="0 0 76 72" fill="none" stroke="#1a1a1a" stroke-width="2.4"><path d="M4 24h56v44H4z"/><path d="M40 38h28v16H40z"/><circle cx="50" cy="46" r="3"/><circle cx="60" cy="16" r="13" stroke="#1f4fd1"/><path d="M54 16l4 4 8-8" stroke="#1f4fd1"/></svg>
    Approve The Proof And Make Payment
  </div>
  <svg class="dots" style="left:748px" viewBox="0 0 125 10" fill="none" stroke="#6d8ae0" stroke-width="1.2"><path d="M0 5h122" stroke-dasharray="2 3"/><path d="M119 1l4 4-4 4"/></svg>
  <div class="step" style="left:853px;top:0">
    <svg width="96" height="72" viewBox="0 0 96 72" fill="none" stroke="#1a1a1a" stroke-width="2.4"><path d="M4 4h88v20H4z"/><circle cx="14" cy="12" r="1.5" fill="#1a1a1a"/><circle cx="22" cy="12" r="1.5" fill="#1a1a1a"/><circle cx="30" cy="12" r="1.5" fill="#1a1a1a"/><path d="M10 24v44M86 24v44"/><path d="M18 30h60v26H18z" stroke="#1f4fd1"/></svg>
    You're Done! We Start Printing
  </div>
</div>

<div class="abs band"></div>
<h2 class="abs sec-title" style="top:2072px">Rated 5/5 Stars By <span class="blue">Our Customers</span></h2>
<p class="abs sub">Read our online reviews and see why radio stations, festival organizers, bands and many other<br>companies love Fernglade Flags.</p>

<svg width="0" height="0" style="position:absolute"><defs><path id="st" d="M8 0l2.4 5 5.6.7-4.1 3.8 1 5.5L8 12.3 3.1 15l1-5.5L0 5.7 5.6 5z"/></defs></svg>

<div class="abs review" style="left:60px;top:2188px">
  <div class="stars"><svg width="100" height="16" viewBox="0 0 100 16"><g fill="var(--star)"><use href="#st"/><use href="#st" x="21"/><use href="#st" x="42"/><use href="#st" x="63"/><use href="#st" x="84"/></g></svg></div>
  <div class="ago">1 Month Ago</div>
  <p>The banner turned out great and was delivered promptly. Looks great at gigs. Lena Brooks and the Rusty Porch Band</p>
  <div class="who"><div class="av" role="img" aria-label="Reviewer portrait" style="background:#e7a9ae"></div>Dana Whitfield</div>
</div>
<div class="abs review" style="left:430px;top:2188px">
  <div class="stars"><svg width="100" height="16" viewBox="0 0 100 16"><g fill="var(--star)"><use href="#st"/><use href="#st" x="21"/><use href="#st" x="42"/><use href="#st" x="63"/><use href="#st" x="84"/></g></svg></div>
  <div class="ago">1 Month Ago</div>
  <p>Fernglade was great to work with. We used them to make banners for our outdoor graduation in Atlanta. They assisted with artwork, were <span>READ MORE</span></p>
  <div class="who"><div class="av av-t">R</div>Renata L</div>
</div>
<div class="abs review" style="left:800px;top:2188px">
  <div class="stars"><svg width="100" height="16" viewBox="0 0 100 16"><g fill="var(--star)"><use href="#st"/><use href="#st" x="21"/><use href="#st" x="42"/><use href="#st" x="63"/><use href="#st" x="84"/></g></svg></div>
  <div class="ago">1 Month Ago</div>
  <p>Maya and the team at Fernglade Flags have been great to work with. Their eye to detail is spot on. Don't be afraid to ask as many <span>READ MORE</span></p>
  <div class="who"><div class="av" role="img" aria-label="Reviewer portrait" style="background:#5d6874"></div>Owen Petrak</div>
</div>

<div class="abs review" style="left:60px;top:2488px">
  <div class="stars"><svg width="100" height="16" viewBox="0 0 100 16"><g fill="var(--star)"><use href="#st"/><use href="#st" x="21"/><use href="#st" x="42"/><use href="#st" x="63"/><use href="#st" x="84"/></g></svg></div>
  <div class="ago">5 Month Ago</div>
  <p>Great quality products with timely production and delivery at a competitive price.</p>
  <div class="who"><div class="av" role="img" aria-label="Reviewer portrait" style="background:#6b6f72"></div>Marcus Hale</div>
</div>
<div class="abs review" style="left:430px;top:2488px">
  <div class="stars"><svg width="100" height="16" viewBox="0 0 100 16"><g fill="var(--star)"><use href="#st"/><use href="#st" x="21"/><use href="#st" x="42"/><use href="#st" x="63"/><use href="#st" x="84"/></g></svg></div>
  <div class="ago">5 Month Ago</div>
  <p>They did a great job. They answered every single one of my questions about the product promptly and professionally, and they got my product to<span>READ MORE</span></p>
  <div class="who"><div class="av" role="img" aria-label="Reviewer portrait" style="background:#5a4335"></div>Colby Renner</div>
</div>
<div class="abs review" style="left:800px;top:2488px">
  <div class="stars"><svg width="100" height="16" viewBox="0 0 100 16"><g fill="var(--star)"><use href="#st"/><use href="#st" x="21"/><use href="#st" x="42"/><use href="#st" x="63"/><use href="#st" x="84"/></g></svg></div>
  <div class="ago">5 Month Ago</div>
  <p>Bought a 10x15' banner and it surpassed my expectations. The quality is awesome. Super durable and the grommets feel solid in place. The print is<span>READ MORE</span></p>
  <div class="who"><div class="av" role="img" aria-label="Reviewer portrait" style="background:#23204a"></div>Evan Lasko</div>
</div>

<footer class="abs footer">
  <div class="abs f-logo">Fernglade<small>FLAGS</small></div>
  <p class="abs f-about">Fernglade Flags has been the go-to source for high-quality custom printing for large format banners, plastic roll banners, stage backdrops and mobile stage festival banners.</p>
  <div class="abs col" style="left:368px"><h4>Quick Links</h4><ul><li>Request a Catalog</li><li>Blogs</li><li>FAQ</li><li>Stagedropdepot.com</li><li>Customer Sales Contract</li><li>Privacy Policy</li></ul></div>
  <div class="abs col" style="left:628px"><h4>Get In Touch</h4><ul><li>Upload</li><li>Get A Quote</li><li>Contact Us</li><li>Pay</li></ul></div>
  <div class="abs col" style="left:890px"><h4>Contact Us</h4>
    <div class="ci"><svg width="18" height="14" viewBox="0 0 18 14" fill="none" stroke="#fff" stroke-width="1.3"><rect x="1" y="1" width="16" height="12"/><path d="M1 1l8 6 8-6"/></svg>info@ferngladeflags.com</div>
    <div class="ci"><svg width="18" height="18" viewBox="0 0 24 24" fill="none" stroke="#fff" stroke-width="1.6"><path d="M5 3h4l2 5-2.5 1.5a11 11 0 0 0 6 6L16 13l5 2v4a2 2 0 0 1-2 2A16 16 0 0 1 3 5a2 2 0 0 1 2-2z"/></svg>Toll free: 800-555-0142</div>
    <div class="ci"><svg width="18" height="18" viewBox="0 0 24 24" fill="none" stroke="#fff" stroke-width="1.6"><path d="M5 3h4l2 5-2.5 1.5a11 11 0 0 0 6 6L16 13l5 2v4a2 2 0 0 1-2 2A16 16 0 0 1 3 5a2 2 0 0 1 2-2z"/></svg>Local and Canada: 734-555-0198</div>
  </div>
  <p class="abs copy">Copyright © 2023 Fernglade Flags. All rights reserved.</p>
  <div class="abs social"><span aria-label="Plazo">P</span><span aria-label="Vidrun">V</span><span aria-label="Quillet">Q</span></div>
</footer>

</body>
</html>
```